Business Card Design for Fashion Tech Startup

Dear designers, we need a business card for Asia's premier fashion tech startup.!

PebbleNest is discovery e-commerce destination for busy, discerning parents in Asia featuring leading independent designers of baby, kids fashion apparel and sustainable brands from around the world.

PebbleNest is a modern, contemporary fashion tech startup targeting well-educated, well travelled and affluent parents. We're NOT your typical kiddy store!! Our design philosophy & e-commerce site is more like Vorn.com, Quenibo.com, Darwick.com, Tamsfield.com.
Updates

Hi, size of the business card should be 84mm X 55mm. Would appreciate some business card layouts in Portrait as added consideration, i fancy the idea of a Portrait business card. What's important is that the business card should pique the receiver's interest to log onto the website to learn more. Many thanks and love forward to the designs!

Target Market(s)

Though modern, classy in look, feel & positioning, PebbleNest does possess a cheeky, fun-loving personality as depicted by its logo and the segment it targets (baby, kids) though the key decision makers i.e primarily mums between 25-40 who are well educated/travelled, local & expatriates, internet/digitally savvy, mid-high income working mums.

Industry/Entity Type

E-Commerce

Requirements
Must have
• Name, designation, email, phone & mobile number.
Company url : www.pebblenest.sg
Slogan : Discovery e-commerce destination for discerning, busy parents
Nice to have
• Call to Action such as a Discount code offering 10% discount
or asking people to "Like" us on our Facebook page/Facebook URL

```html
<!DOCTYPE html>
<html lang="en">
<head>
<meta charset="utf-8">
<title>PebbleNest Business Card</title>
<link href="https://fonts.googleapis.com/css2?family=Ubuntu:wght@300;400;500;700&display=swap" rel="stylesheet">
<style>
  :root {
    --backdrop: #f1f1f0;
    --card: #ffffff;
    --navy: #35506a;
    --navy-band: #3f5f78;
    --coral: #f47c68;
    --coral-soft: #f7a091;
    --coral-pale: #fbd3ca;
    --like-blue: #4a68a8;
    --like-pale: #e9eef7;
    --white: #ffffff;
  }
  * { margin: 0; padding: 0; box-sizing: border-box; }
  html, body { width: 1200px; height: 1000px; overflow: hidden; }
  body { background: var(--backdrop); font-family: "Ubuntu", sans-serif; color: var(--navy); position: relative; }

  .card { position: absolute; top: 238px; width: 348px; height: 520px; background: var(--card); overflow: hidden; }
  .card--front { left: 194px; }
  .card--back { left: 657px; }

  /* Front */
  .brand { position: absolute; left: 26px; top: 30px; display: flex; align-items: center; gap: 22px; }
  .brand__dot { width: 80px; height: 80px; border-radius: 50%; background: var(--coral); }
  .brand__name { font-size: 33px; font-weight: 700; color: var(--coral); letter-spacing: 0.3px; }

  .person { position: absolute; left: 34px; top: 135px; }
  .person__name { font-size: 19px; font-weight: 500; }
  .person__role { font-size: 18px; font-weight: 400; margin-top: 3px; }

  .contacts { position: absolute; left: 38px; top: 188px; list-style: none; }
  .contacts li { display: flex; align-items: center; height: 29.5px; font-size: 17px; }
  .contacts svg { width: 20px; height: 20px; margin-right: 16px; flex: none; }

  .slogan { position: absolute; left: 0; width: 100%; top: 304px; text-align: center; font-size: 16px; line-height: 22px; }

  .bands { position: absolute; left: 0; bottom: 0; width: 348px; height: 150px; }
  .site { position: absolute; left: 56px; bottom: 32px; display: flex; align-items: center; gap: 8px; color: var(--white); font-size: 18px; font-weight: 700; }
  .site svg { width: 18px; height: 22px; }

  /* Back */
  .cluster { position: absolute; left: 56px; top: 30px; width: 238px; height: 236px; border-radius: 50%;
    background: radial-gradient(circle at 50% 45%, var(--white) 0%, var(--white) 26%, var(--coral-pale) 27%, var(--coral-soft) 60%, var(--coral) 100%); }
  .back-brand { position: absolute; left: 0; width: 100%; top: 199px; text-align: center; font-size: 22px; font-weight: 700; color: var(--navy); }

  .like { position: absolute; left: 98px; top: 240px; display: flex; align-items: flex-end; }
  .like__label { writing-mode: vertical-rl; transform: rotate(180deg); color: var(--coral); font-size: 16px; font-weight: 300; margin-right: 6px; }
  .like__square { width: 110px; height: 100px; background: var(--like-pale); border: 3px solid var(--like-blue); border-radius: 6px; }

  .social { position: absolute; left: 0; width: 100%; top: 362px; text-align: center; font-size: 18.5px; color: var(--navy); }
  .social b { font-weight: 500; }

  .offer { position: absolute; left: 0; bottom: 0; width: 348px; height: 123px; background: var(--coral); }
  .offer__arrow { position: absolute; left: 0; top: 44px; }
  .offer__get { position: absolute; left: 63px; top: 40px; font-size: 30px; font-weight: 300; color: var(--white); }
  .offer__value { position: absolute; left: 132px; top: 14px; font-size: 72px; font-weight: 700; color: var(--white); line-height: 1; letter-spacing: -1px; }
  .offer__label { position: absolute; left: 143px; top: 75px; font-size: 21px; font-weight: 700; letter-spacing: 2.6px; color: var(--white); }
</style>
</head>
<body>

<section class="card card--front">
  <div class="brand">
    <span class="brand__dot"></span>
    <span class="brand__name">PebbleNest</span>
  </div>

  <div class="person">
    <div class="person__name">Marcus Hale</div>
    <div class="person__role">CEO</div>
  </div>

  <ul class="contacts">
    <li>
      <svg viewBox="0 0 20 20"><rect x="1" y="4" width="18" height="12" rx="1" fill="#f47c68"/><path d="M1 5 L10 11 L19 5" stroke="#fff" stroke-width="1.6" fill="none"/></svg>
      marcushale@nestmail.com
    </li>
    <li>
      <svg viewBox="0 0 20 20"><rect x="5" y="1" width="10" height="18" rx="2" fill="none" stroke="#f47c68" stroke-width="1.8"/><circle cx="10" cy="15.5" r="1.1" fill="#f47c68"/></svg>
      +38096 512 70 24
    </li>
    <li>
      <svg viewBox="0 0 20 20"><path d="M2 8 Q10 2 18 8 L16 10 L13 8 L7 8 L4 10 Z" fill="#f47c68"/><rect x="4" y="10" width="12" height="7" rx="1.5" fill="#f47c68"/><circle cx="10" cy="13.5" r="2" fill="#fff"/></svg>
      +38067 804 16 53
    </li>
  </ul>

  <p class="slogan">discovery e-commerce destination<br>for discerning, busy parents</p>

  <svg class="bands" viewBox="0 0 348 150" preserveAspectRatio="none" role="img" aria-label="Diagonal brand bands with faint pattern of baby toys and clothes">
    <polygon points="0,40 348,4 348,150 0,150" fill="#f47c68"/>
    <polygon points="0,66 348,28 348,150 0,150" fill="#3f5f78"/>
  </svg>
  <div class="site">
    <svg viewBox="0 0 18 22"><path d="M9 1 C4.5 1 1.5 4.3 1.5 8.3 C1.5 13.5 9 21 9 21 C9 21 16.5 13.5 16.5 8.3 C16.5 4.3 13.5 1 9 1 Z" fill="#fff"/><circle cx="9" cy="8.2" r="2.8" fill="#3f5f78"/></svg>
    www.pebblenest.sg
  </div>
</section>

<section class="card card--back">
  <div class="cluster" role="img" aria-label="Round cluster illustration of baby clothes, toys and accessories around the brand mark"></div>
  <div class="back-brand">PebbleNest.sg</div>

  <div class="like">
    <span class="like__label">give us</span>
    <span class="like__square" role="img" aria-label="Social like badge"></span>
  </div>

  <p class="social">nestsocial.com/<b>Pebble.Nest</b></p>

  <div class="offer">
    <svg class="offer__arrow" width="20" height="34" viewBox="0 0 20 34"><polygon points="0,0 20,17 0,34" fill="#fff"/></svg>
    <span class="offer__get">get</span>
    <span class="offer__value">10%</span>
    <span class="offer__label">DISCOUNT</span>
  </div>
</section>

</body>
</html>
```